Pool business needs attractive flyer

I just started my own pool service business, Here is the Information I want on the flyer but you put it anyway you think best.

Service Call $45
which Includes: Chemical Balance, Inspect all equipment, Skim water surface, clean filters.

Vacuum $10
Please Call, txt or Email for chemical price list

Other Services Include:
Supply and install Pumps, Chlorinators, Automatic Cleaners & Spare Parts

My Name
0438215967
TidesMail@vorlix.com

Pool Service

```html
<!DOCTYPE html>
<html lang="en">
<head>
<meta charset="utf-8">
<title>Pool Service Flyer</title>
<link rel="stylesheet" href="https://fonts.googleapis.com/css2?family=Barlow:wght@600&family=Barlow+Condensed:wght@400;600&family=Arimo&display=swap">
<style>
  :root {
    --sky: #03adef;
    --orange: #f7941d;
    --green: #3cb54a;
    --pink: #ec1461;
    --navy: #1b5ea8;
    --white: #ffffff;
    --paper: #ffffff;
  }
  * { margin: 0; padding: 0; box-sizing: border-box; }
  html, body { width: 1200px; height: 848px; overflow: hidden; background: var(--paper); }
  .flyer { position: relative; width: 1200px; height: 848px; background: var(--paper); color: var(--white); }

  .contact-band {
    position: absolute; left: 0; top: 0; width: 790px; height: 235px;
    background: var(--sky); text-align: center;
  }
  .owner-name {
    font-family: "Barlow", sans-serif; font-weight: 600;
    font-size: 108px; letter-spacing: 6px; line-height: 1;
    margin-top: 20px;
  }
  .owner-phone, .owner-email { font-family: "Arimo", sans-serif; line-height: 1; }
  .owner-phone { font-size: 36px; margin-top: 6px; }
  .owner-email { font-size: 40px; margin-top: 4px; }

  .brand {
    position: absolute; left: 830px; top: 40px; width: 340px; height: 160px;
    display: flex; align-items: center; gap: 18px;
  }
  .brand-dot { width: 46px; height: 46px; border-radius: 50%; background: var(--sky); flex: none; }
  .brand-name {
    font-family: "Barlow Condensed", sans-serif; font-weight: 600;
    font-size: 58px; line-height: 0.95; color: var(--navy); text-transform: uppercase;
  }

  .service-arrows { position: absolute; left: 0; top: 0; }

  .panel { position: absolute; font-family: "Barlow Condensed", sans-serif; text-transform: uppercase; }
  .panel-title {
    font-weight: 600; font-size: 90px; line-height: 74px; text-align: center;
  }
  .panel-text { font-weight: 400; font-size: 47px; line-height: 53px; }

  .panel-service { left: 10px; top: 300px; width: 380px; }
  .panel-service .panel-title { width: 330px; }
  .panel-vacuum { left: 436px; top: 300px; width: 380px; }
  .panel-vacuum .panel-title { width: 310px; }
  .panel-vacuum .panel-text { margin-top: 12px; }
  .panel-other { left: 888px; top: 300px; width: 310px; }
  .panel-other .panel-title { width: 300px; }
  .panel-service .panel-text { margin-top: 6px; }
  .panel-other .panel-text { margin-top: 14px; }
</style>
</head>
<body>
<main class="flyer">
  <header class="contact-band">
    <h1 class="owner-name">MY NAME</h1>
    <p class="owner-phone">0438215967</p>
    <p class="owner-email">TIDESMAIL@VORLIX.COM</p>
  </header>

  <div class="brand">
    <span class="brand-dot"></span>
    <span class="brand-name">Clearwave<br>Pool Care</span>
  </div>

  <svg class="service-arrows" width="1200" height="848" viewBox="0 0 1200 848" aria-hidden="true">
    <polygon fill="var(--orange)" points="0,272 326,272 397,534 326,807 0,807"/>
    <polygon fill="var(--green)" points="358,272 780,272 848,534 780,807 366,807 422,534"/>
    <polygon fill="var(--pink)" points="814,267 1200,267 1200,807 818,807 882,534"/>
  </svg>

  <section class="panel panel-service">
    <h2 class="panel-title">Service<br>Call $45</h2>
    <p class="panel-text">Includes: Chemical<br>Balance, Inspect<br>All Equipment,<br>Skim Water<br>Surface, Clean<br>Filters.</p>
  </section>

  <section class="panel panel-vacuum">
    <h2 class="panel-title">Vacuum<br>$10</h2>
    <p class="panel-text">Please Call, Text<br>or Email for Che-<br>mical Price List.</p>
  </section>

  <section class="panel panel-other">
    <h2 class="panel-title">Other<br>Services</h2>
    <p class="panel-text">Supply and<br>Install Pumps,<br>Chlorinators,<br>Automatic<br>Cleaners &amp;<br>Spare Parts.</p>
  </section>
</main>
</body>
</html>
```